Wheatless Table Co Web Design

We are looking for designs for a homepage for a gluten free, health food website.

We are looking for the site to be a shop, as well as a resource/information source for users. We will also look to incorporate recipes, blogs, forums and potentially some other useful information.

We want to ensure that the website is user-friendly, does not have a corporate feel, but is still classy.

We want to have high quality photographic images in the background, with text in the foreground - but these things will need to compliment each other well. e.g recipe of the week integrated onto the background photo and the 'shop' in the foreground.

We have seen a site that we quite like and although we like the design, we do not want to completely emulate this. However, it is a useful starting point for designers and perhaps some inspiration www.brambleharvestgrocer.example

We already have a logo - see attached - which will need to be fully integrated into the design.

We do want a colourful design, but mainly in terms of the images rather than the graphics.
Updates

Please note:

We are pleased with the designs to date, for the most part. We would like you all to note, however, that we are much preferring the lighter designs - ones that make the sites feel brighter - rather than those which are darker in appearance.

We would also like to see less space allocated to the main image, within the context of the site as a whole.

Thanks.

We have eliminated those which we feel are not what we are looking for. We are still keen to see some more designs and are still looking for something unique. There are some good things in all of the designs that we have not eliminated, however we still feel there is room for more inspiration.

Thanks.

Target Market(s)

Our audience are body conscience people looking for health food products. They are also those who are potentially looking for a new lifestyle/life cha

Industry/Entity Type

Health

Requirements
Must have
• Our logo - attached, can provide variations in due course.

Navigational features as per mock up attached.

Social network integration.

NB: we only need one (home) page for this.

```html
<!DOCTYPE html>
<html lang="en">
<head>
<meta charset="utf-8">
<title>Wheatless Table Co</title>
<link rel="stylesheet" href="https://fonts.googleapis.com/css2?family=Lobster&family=Oswald:wght@500;700&family=Open+Sans:wght@400;600;700&family=Rubik+Dirt&display=swap">
<style>
:root{
  --red:#c8141b;
  --red-dark:#8e0a0e;
  --black:#111;
  --ink:#333;
  --muted:#777;
  --white:#fff;
  --wood-a:#e6cfb0;
  --wood-b:#d9bb95;
  --sky:#35b3ee;
  --footer:#1d1b1a;
  --panel:#f3f3f3;
}
*{box-sizing:border-box;margin:0;padding:0}
html,body{width:1200px;height:1046px;overflow:hidden}
body{position:relative;font-family:"Open Sans",Arial,sans-serif;color:var(--ink);background:linear-gradient(90deg,var(--wood-a),var(--wood-b) 30%,var(--wood-a) 60%,var(--wood-b))}
.abs{position:absolute}

/* hero */
.hero{left:0;top:0;width:1200px;height:454px;background:linear-gradient(90deg,#b80f14 0%,#d2161c 30%,#c41218 100%)}
.hero-photo{left:300px;top:0;width:900px;height:454px;background:radial-gradient(ellipse at 45% 65%,#e9a24a 0%,#c0621f 22%,#7a3a1a 40%,rgba(190,20,25,.2) 70%),linear-gradient(90deg,rgba(200,20,27,1) 0%,rgba(120,40,30,.7) 35%,rgba(200,20,27,.7) 100%)}
.hero-title{left:490px;top:150px;width:420px;text-align:center;font-family:"Lobster",cursive;font-size:50px;font-weight:400;color:var(--white);text-shadow:0 2px 4px rgba(0,0,0,.4);white-space:nowrap}
.ribbon{left:535px;top:231px;width:322px;height:43px;background:var(--red);color:var(--white);font-size:23px;line-height:43px;text-align:center;white-space:nowrap;box-shadow:0 3px 6px rgba(0,0,0,.35)}
.shop-now{left:586px;top:274px;width:216px;height:29px;background:var(--black);color:var(--white);font-weight:700;font-size:17px;line-height:29px;text-align:center;white-space:nowrap}
.dots{left:1047px;top:424px;display:flex;gap:6px}
.dots span{width:10px;height:10px;border-radius:50%;background:var(--white)}
.dots span.on{background:transparent;border:2px solid var(--white)}

/* top bar */
.topbar{left:729px;top:0;width:356px;height:46px;background:var(--black);display:flex;align-items:center;padding-left:18px}
.topbar a{color:var(--white);font-size:11px;line-height:14px;text-decoration:none;padding:0 9px;border-right:1px solid #555;white-space:nowrap;flex:none}
.topbar a:last-of-type{border-right:0}
.search{margin-left:auto;margin-right:10px;width:170px;flex:none;height:22px;border-radius:11px;background:var(--white);font-size:10px;color:#999;line-height:22px;padding-left:12px;position:relative}
.search svg{position:absolute;right:8px;top:5px}

/* sidebar */
.sidebar{left:113px;top:120px;width:192px;height:334px;background:var(--black)}
.brand{left:146px;top:57px;width:136px;height:136px;border-radius:50%;background:var(--black);border:3px solid var(--white);display:flex;align-items:center;justify-content:center;text-align:center;color:var(--white);font-weight:700;font-size:18px;line-height:1.15;padding:10px}
.nav{left:113px;top:202px;width:192px;list-style:none;text-align:center}
.nav li{font-family:"Rubik Dirt",fantasy;font-size:25px;color:var(--white);height:37px;line-height:37px;white-space:nowrap}
.follow{left:158px;top:420px;width:102px;height:80px;border-radius:0 0 51px 51px;background:var(--black);text-align:center;color:var(--white)}
.follow p{font-family:"Lobster",cursive;font-size:14px;margin-top:26px}
.follow .icons{display:flex;justify-content:center;gap:4px;margin-top:4px}
.follow .icons span{width:14px;height:14px;border-radius:50%;background:var(--white)}

.submenu{left:309px;top:266px;width:145px;height:134px;background:rgba(240,240,240,.92);list-style:none;padding:10px 0 0 18px}
.submenu li{font-size:12px;color:#222;height:30px;line-height:30px;white-space:nowrap}

/* section headings */
.heading{font-family:"Oswald",sans-serif;font-weight:700;font-size:18px;color:#111;letter-spacing:.3px}
.pager{display:flex;gap:3px}
.pager span{width:14px;height:14px;border-radius:50%;background:#bbb;display:flex;align-items:center;justify-content:center}
.pager span.next{background:var(--red)}

.feat-img{left:317px;top:533px;width:281px;height:276px;background:radial-gradient(ellipse at 50% 45%,#e7b04a 0%,#c96a2a 35%,#5b7a2a 55%,#2a2a22 85%)}
.tag{left:309px;height:31px;background:var(--red);color:var(--white);font-size:17px;line-height:31px;padding-left:18px;white-space:nowrap;box-shadow:0 2px 4px rgba(0,0,0,.3)}

.tweet{left:317px;top:824px;width:281px;height:110px;background:var(--sky);color:var(--white);font-size:10.5px;line-height:1.45;padding:20px 10px 0 12px}
.tweet .who{color:#e3f5ff;margin-bottom:3px;font-size:11px}
.tweet-dot{left:310px;top:816px;width:16px;height:16px;border-radius:50%;background:var(--white)}

/* blogs */
.blogs{left:614px;top:533px;width:471px;height:276px;background:var(--white)}
.divider{left:849px;top:533px;width:2px;height:276px;background:#e3e3e3}
.card{top:543px;width:218px}
.card .img{height:134px}
.card h3{font-weight:400;color:var(--red);font-size:14px;margin:12px 0 6px 8px;white-space:nowrap}
.card p{font-size:11px;line-height:1.4;color:#777;margin:0 8px}
.card .meta{display:flex;justify-content:space-between;font-size:9.5px;color:#888;margin:14px 8px 0;align-items:center;white-space:nowrap}
.card .meta b{color:#222;font-weight:600;font-size:10.5px}

/* forum */
.forum{left:614px;top:828px;width:471px;height:106px;background:var(--white)}
.forum-head{height:24px;background:var(--red);color:var(--white);display:flex;align-items:center;font-size:14px;white-space:nowrap}
.forum-head .t{flex:1;padding-left:16px}
.forum-head .c{width:60px;text-align:center;font-size:10.5px}
.forum-head .d{width:114px;text-align:center;font-size:10.5px}
.forum-row{display:flex;height:82px}
.forum-row .t{flex:1;padding:8px 16px;border-right:1px solid #e3e3e3}
.forum-row .t h4{font-weight:400;color:var(--red);font-size:14px;margin-bottom:4px;white-space:nowrap}
.forum-row .t p{font-size:10.5px;line-height:1.35;color:#555}
.forum-row .c{width:60px;text-align:center;font-size:11px;padding-top:28px;border-right:1px solid #e3e3e3}
.forum-row .d{width:114px;text-align:center;font-size:10.5px;padding-top:28px;white-space:nowrap}

/* footer */
.footer{left:0;top:986px;width:1200px;height:60px;background:var(--footer)}
.footer nav{position:absolute;left:115px;top:20px;display:flex;gap:22px}
.footer a{color:#ddd;font-size:12px;text-decoration:none;white-space:nowrap}
.footer .mark{position:absolute;right:110px;top:18px;font-weight:700;font-size:16px;color:#3a3735;white-space:nowrap}
</style>
</head>
<body>

<section class="abs hero" aria-label="Recipe of the week">
  <div class="abs hero-photo" role="img" aria-label="Close-up photo of a chipotle burger with leafy greens"></div>
</section>
<h1 class="abs hero-title">Recipe Of The Week</h1>
<div class="abs ribbon">Chipotle Burger - $1.99 a pint</div>
<div class="abs shop-now">Shop Now
  <svg width="12" height="12" viewBox="0 0 12 12" style="vertical-align:-1px"><circle cx="6" cy="6" r="6" fill="#fff"/><path d="M5 3l3 3-3 3" stroke="#111" stroke-width="1.6" fill="none"/></svg>
</div>
<div class="abs dots"><span></span><span class="on"></span><span></span></div>

<header class="abs topbar">
  <a href="#">Home</a><a href="#">Log In</a><a href="#">Contact Us</a>
  <div class="search">Search
    <svg width="11" height="11" viewBox="0 0 11 11"><circle cx="4.5" cy="4.5" r="3.5" stroke="#555" stroke-width="1.4" fill="none"/><path d="M7 7l3 3" stroke="#555" stroke-width="1.4"/></svg>
  </div>
</header>

<aside class="abs sidebar"></aside>
<div class="abs brand">Wheatless Table Co</div>
<ul class="abs nav">
  <li>SHOP</li><li>OUR STORY</li><li>BLOG</li><li>HINTS &amp; TIPS</li><li>RECIPES</li><li>FORUMS</li>
</ul>
<div class="abs follow">
  <p>Follow us on</p>
  <div class="icons"><span></span><span></span><span></span><span></span></div>
</div>
<ul class="abs submenu">
  <li>Kids Pizza</li><li>Gluten Free sCones</li><li>Organic Food</li><li>Summer Foods</li>
</ul>

<h2 class="abs heading" style="left:317px;top:500px">FEATURED RECIPE</h2>
<div class="abs pager" style="left:570px;top:507px"><span></span><span class="next"><svg width="6" height="8" viewBox="0 0 6 8"><path d="M1 1l3 3-3 3" stroke="#fff" stroke-width="1.5" fill="none"/></svg></span></div>
<div class="abs feat-img" role="img" aria-label="Photo of a paella with prawns and green beans"></div>
<div class="abs tag" style="top:732px;width:140px">Tumbled</div>
<div class="abs tag" style="top:770px;width:140px">Traditionally</div>

<div class="abs tweet">
  <p class="who">Wheatless Table Co @wheatlesstable</p>
  <p>How wonderful, a gluten free travel agency. They pre-arrange gluten free travel arrangements... http://www.wheatlesstravel.example</p>
</div>
<div class="abs tweet-dot"></div>

<h2 class="abs heading" style="left:614px;top:500px">BLOGS</h2>
<div class="abs pager" style="left:1057px;top:507px"><span></span><span class="next"><svg width="6" height="8" viewBox="0 0 6 8"><path d="M1 1l3 3-3 3" stroke="#fff" stroke-width="1.5" fill="none"/></svg></span></div>
<div class="abs blogs"></div>
<div class="abs divider"></div>

<article class="abs card" style="left:622px">
  <div class="img" role="img" aria-label="Photo of strawberries and blueberries" style="background:radial-gradient(circle at 40% 60%,#e0242a,#a3101a 50%,#2a2a4a 90%)"></div>
  <h3>Blueberries on Sale Today Only</h3>
  <p>Lorem Ipsum is simply dummy text of the printing and typesetting industry. Lorem Ipsum has been the industry's standard dummy text ever since...</p>
  <div class="meta"><span>&#9635; MAY, 31, 2013</span><b>by Marla Quint</b></div>
</article>
<article class="abs card" style="left:859px">
  <div class="img" role="img" aria-label="Photo of a wrap filled with fresh vegetables" style="background:radial-gradient(circle at 50% 50%,#e98a3a,#b8c27a 45%,#d9cdb0 80%)"></div>
  <h3>Get Your Morning Veggies</h3>
  <p>Lorem Ipsum is simply dummy text of the printing and typesetting industry. Lorem Ipsum has been the industry's standard dummy text ever since...</p>
  <div class="meta"><span>&#9635; MAY, 31, 2013</span><b>by Teo Barrowe</b></div>
</article>

<section class="abs forum">
  <div class="forum-head"><span class="t">Healthy Eating Forums</span><span class="c">Replies</span><span class="d">Last Post</span></div>
  <div class="forum-row">
    <div class="t">
      <h4>Introductions &amp; Personal Stories</h4>
      <p>Healthy Eating Support Group members are welcome to introduce themselves. Tell your story, share experiences, success stories and failures.</p>
    </div>
    <div class="c">12</div>
    <div class="d">03/15/2013 03:46 PM</div>
  </div>
</section>

<footer class="abs footer">
  <nav><a href="#">Contact</a><a href="#">Site Map</a><a href="#">FAQ's</a><a href="#">Privacy Policy</a></nav>
  <span class="mark">Wheatless Table Co</span>
</footer>

</body>
</html>
```